Business Card Design Project

We need a business card design for an existing company in Dallas/Fort Worth that is expanding services and re-branding. We are changing the name from Brightmoor Commercial Cleaning to Keystride Facility Services. We are expanding from only commercial cleaning to include complete commercial landscape and facility maintenance services, too.

As stated, we offer a package of services that includes landscape, janitorial and facility services, which is largely unique in the industry.

We would like a design that communicates trust/partnership with a professional, corporate image, but not necessarily using the standard white business card. We would like a design that perhaps uses darker blues or perhaps a gray background, but we are open to other ideas. We might also be interested in a double-sided design - maybe with our logo on the back, printed on a gray background?

We will probably stick with the attached logo, but if you've got another inspired idea....

Target Market(s)

Property managers, commercial real estate professionals, corporate executives

Industry/Entity Type

Landscape

Requirements
Should not have
• Not interested in old style fonts.

```html
<!DOCTYPE html>
<html lang="en">
<head>
<meta charset="utf-8">
<title>Keystride Facility Services – Business Cards</title>
<link rel="stylesheet" href="https://fonts.googleapis.com/css2?family=Questrial&display=swap">
<style>
  :root{
    --navy-deep:#0b1f45;
    --navy:#143a78;
    --blue-glow:#2160b8;
    --ink:#1c2f5c;
    --paper:#eef0f3;
    --rule:#ffffff;
    --text-dark:#222a36;
    --backdrop:#d9dce1;
  }
  *{margin:0;padding:0;box-sizing:border-box}
  html,body{width:1067px;height:1200px;overflow:hidden;background:var(--backdrop)}
  body{position:relative;font-family:"Questrial",Arial,sans-serif;color:var(--text-dark)}

  .card{
    position:absolute;left:153px;width:760px;height:434px;
    background:var(--paper);overflow:hidden;
    box-shadow:0 10px 28px rgba(0,0,0,.28);
  }
  .card--front{top:90px}
  .card--back{top:660px}

  /* Front */
  .band{position:absolute;left:0;width:100%;
    background:linear-gradient(180deg,var(--navy) 0%,var(--navy-deep) 100%)}
  .band--top{top:0;height:52px;border-bottom:3px solid var(--rule);box-shadow:0 5px 0 var(--navy-deep)}
  .band--bottom{bottom:0;height:78px;border-top:3px solid var(--rule);box-shadow:0 -5px 0 var(--navy-deep);
    display:flex;align-items:center;justify-content:center}
  .website{color:#dfe6f2;font-size:19px;letter-spacing:1px}

  .brand{position:absolute;display:flex;align-items:center;gap:14px}
  .card--front .brand{left:70px;top:150px}
  .brand__mark{border:6px solid var(--ink);flex:none}
  .card--front .brand__mark{width:96px;height:96px}
  .brand__name{color:var(--ink);text-transform:uppercase;line-height:1}
  .brand__name span{display:block}
  .card--front .brand__primary{font-size:56px;letter-spacing:3px}
  .card--front .brand__secondary{font-size:33px;letter-spacing:2px;margin-top:4px}
  .tagline{position:absolute;color:var(--ink);font-size:14.5px;font-weight:400}
  .card--front .tagline{left:180px;top:262px}

  /* Back */
  .back__header{position:absolute;left:0;top:0;width:100%;height:200px;
    background:radial-gradient(ellipse 340px 180px at 52% 85%,var(--blue-glow) 0%,var(--navy) 45%,var(--navy-deep) 100%);
    border-bottom:3px solid var(--rule);box-shadow:0 6px 0 var(--navy-deep)}
  .back__stripe{position:absolute;top:0;left:470px;width:70px;height:200px;background:rgba(255,255,255,.09)}
  .card--back .brand{left:50px;top:62px}
  .card--back .brand__mark{width:58px;height:58px;border:4px solid #fff}
  .card--back .brand__name{color:#fff}
  .card--back .brand__primary{font-size:38px;letter-spacing:2px}
  .card--back .brand__secondary{font-size:24px;letter-spacing:1.5px;margin-top:2px}
  .card--back .tagline{left:122px;top:128px;color:#fff;font-size:10.5px}

  .person{position:absolute;left:70px;top:262px}
  .person__name{color:var(--navy);font-size:24px}
  .person__role{font-size:17px;margin-top:2px}
  .contact{list-style:none;margin-top:20px;font-size:16px;line-height:1.25}
  .contact b{color:var(--navy);font-weight:400}

  .office{position:absolute;left:400px;top:228px;padding-left:14px;border-left:1.5px solid #9aa3b0;font-size:16px;line-height:1.3}
  .office .contact{margin-top:22px}
</style>
</head>
<body>

<section class="card card--front" aria-label="Business card front">
  <div class="band band--top"></div>
  <div class="brand">
    <div class="brand__mark"></div>
    <div class="brand__name"><span class="brand__primary">Keystride</span><span class="brand__secondary">Facility Services</span></div>
  </div>
  <p class="tagline">One Source For Landscape, Janitorial and Facility Maintenance</p>
  <div class="band band--bottom"><span class="website">www.keystridefacilityservices.com</span></div>
</section>

<section class="card card--back" aria-label="Business card back">
  <div class="back__header"><div class="back__stripe"></div></div>
  <div class="brand">
    <div class="brand__mark"></div>
    <div class="brand__name"><span class="brand__primary">Keystride</span><span class="brand__secondary">Facility Services</span></div>
  </div>
  <p class="tagline">One Source For Landscape, Janitorial and Facility Maintenance</p>

  <div class="person">
    <p class="person__name">Marcus Redfield</p>
    <p class="person__role">General manager</p>
    <ul class="contact">
      <li><b>p:</b> +(00) 00 0000 0000</li>
      <li><b>f:</b> +(00) 00 0000 0000</li>
    </ul>
  </div>

  <div class="office">
    <p>Keystride Facility Center</p>
    <p>Harlow Park, Fort Worth, Texas</p>
    <p>www.keystridefacilityservices.com</p>
    <ul class="contact">
      <li><b>e:</b> info@keystridefacilityservices.com</li>
      <li><b>w:</b> www.keystridefacilityservices.com</li>
    </ul>
  </div>
</section>

</body>
</html>
```